Graphic to hang inside of fitness studio

This graphic will be printed on vinyl and hung inside of a boutique fitness studio for 2019. Graphic should read YEAR OF POSSIBILITIES.

2018 was called Year of Living Well. We would like something on trend for 2019 to hang within the studio as our 2019 Mantra. It is not a logo but for internal use. I've attached our logo here and the website is www.kestrelmovehall.com for additional reference. Thank you.

Target Market(s)

25 to 45 women

Industry/Entity Type

Fitness

Colors

Designer to choose colors to be used in the design.

Requirements
Must have
• On trend for 2019. (no people in image)
• Year of Possibilities in trendy font.
• Easy to read.
• Need text only.
• Do not need graphic images.
Nice to have
• Tintorell colours for 2019
• 2019 design trends for background
Should not have
• Male dominate colour or masculine traits.
• Photos of fitness.
• Photos of people.
• Photos of equipment.

```html
<!DOCTYPE html>
<html lang="en">
<head>
<meta charset="utf-8">
<title>Year of Possibilities — Kestrel Move Hall 2019 Mantra</title>
<link rel="stylesheet" href="https://fonts.googleapis.com/css2?family=Yellowtail&family=Lobster&family=Oswald:wght@600&display=block">
<style>
  :root {
    --bg-base: #e9616b;
    --bg-deep-red: #a9182b;
    --bg-amber: #e8b443;
    --bg-orange: #e0683f;
    --bg-mauve: #c0656f;
    --bg-pink: #f68c8b;
    --script-fill: #86e6e8;
    --script-shadow: #226a6b;
    --brand-ink: #3d6b6b;
  }
  html, body {
    margin: 0;
    padding: 0;
    width: 1200px;
    height: 600px;
    overflow: hidden;
  }
  .mantra-banner {
    position: relative;
    width: 1200px;
    height: 600px;
    overflow: hidden;
    background:
      radial-gradient(ellipse 320px 260px at 540px 250px, var(--bg-deep-red) 0%, rgba(169,24,43,0) 100%),
      radial-gradient(ellipse 360px 200px at 780px 10px, var(--bg-amber) 0%, rgba(232,180,67,0) 100%),
      radial-gradient(ellipse 420px 260px at 640px 140px, var(--bg-orange) 0%, rgba(224,104,63,0) 100%),
      radial-gradient(ellipse 380px 300px at 60px 80px, var(--bg-mauve) 0%, rgba(192,101,111,0) 100%),
      radial-gradient(ellipse 460px 300px at 1080px 520px, var(--bg-pink) 0%, rgba(246,140,139,0) 100%),
      var(--bg-base);
  }
  .soft-blob {
    position: absolute;
    right: -60px;
    top: 200px;
    width: 260px;
    height: 200px;
    border-radius: 50%;
    background: rgba(214, 96, 110, 0.35);
  }
  .mantra-tails {
    position: absolute;
    inset: 0;
  }
  .mantra-title {
    margin: 0;
    font-weight: 400;
  }
  .mantra-word {
    position: absolute;
    margin: 0;
    font-family: "Yellowtail", "Lobster", cursive;
    font-weight: 400;
    color: var(--script-fill);
    line-height: 1;
    text-shadow: 2px 2px 0 var(--script-shadow), 4px 5px 0 var(--script-shadow);
    white-space: nowrap;
  }
  .mantra-year {
    left: 200px;
    top: 118px;
    font-size: 140px;
  }
  .mantra-of {
    left: 505px;
    top: 208px;
    font-size: 72px;
  }
  .mantra-possibilities {
    left: 218px;
    top: 262px;
    font-size: 150px;
  }
  .brand-name {
    position: absolute;
    right: 40px;
    bottom: 28px;
    margin: 0;
    font-family: "Oswald", sans-serif;
    font-weight: 600;
    font-size: 15px;
    letter-spacing: 0.3px;
    color: var(--brand-ink);
  }
</style>
</head>
<body>
  <main class="mantra-banner">
    <div class="soft-blob"></div>

    <svg class="mantra-tails" width="1200" height="600" viewBox="0 0 1200 600" aria-hidden="true">
      <g fill="var(--script-shadow)" transform="translate(4 5)">
        <path d="M215 262 C 300 266 380 270 448 270 L 425 298 C 360 284 290 272 215 262 Z"/>
        <path d="M700 402 C 820 408 920 406 1002 394 L 790 462 C 770 440 740 420 700 402 Z"/>
      </g>
      <g fill="var(--script-fill)">
        <path d="M215 262 C 300 266 380 270 448 270 L 425 298 C 360 284 290 272 215 262 Z"/>
        <path d="M700 402 C 820 408 920 406 1002 394 L 790 462 C 770 440 740 420 700 402 Z"/>
      </g>
    </svg>

    <h1 class="mantra-title">
      <span class="mantra-word mantra-year">Year</span>
      <span class="mantra-word mantra-of">of</span>
      <span class="mantra-word mantra-possibilities">Possibilities</span>
    </h1>

    <p class="brand-name">KESTREL MOVE HALL</p>
  </main>
</body>
</html>
```